General Surgeon flyer to be distributed to GPs

I am a general surgeon and I would like to have a flyer designed aiming to introduce myself to GPs.

Name: Dr Tobias Vanterpool MD, FHCS
Address: Suite 4C, Brindle private hospital, 518 Cobbler Parade, Wantirna, VIC, 3152
T: (03) 9587 1062
F: (03) 9316 4471
E: referrals@lanternoperativeclinic.com.au
Website: www.lanternoperativeclinic.com.au

Tobias is a highly trained general surgeon, having completed extensive surgical training at Coralbay health, Fenwick and Thornleigh Health networks. He further specialized by completing a fellowship in Oesophagogastric and Bariatric Surgery at Larkspur Hospital Northgate, one of Northridge’s leading Upper GI surgical centres.

With expertise in both advanced laparoscopic and open surgical techniques, he performs a wide range of procedures involving the gastrointestinal system, abdominal wall hernias, as well as other major and minor general surgical operations. In addition to holding appointments at Coralbay Health, he also operates at Brindle and Quarrydale Private Hospitals.

Dr Vanterpool is committed to providing patient-centred care with a focus on surgical precision, safety, and long-term health outcomes.

He is also fluent in Farsi/Pesrian.
Outside of surgery, Tobias enjoys playings classical piano and spending time with his 6-year-old Bordoodle on long walks.

Upper GI & Bariatric Surgery:
Hiatus hernia repair, sleeve gastrectomy, gastric bypass
General Surgery conditions:
Gallbladder Surgery: Laparoscopic cholecystectomy
Hernia Repair: Laparoscopic and open surgery (inguinal,
umbilical, incisional)
Anorectal Procedures: Haemorrhoidectomy, haemorrhoid banding
Hand Surgery: Carpal tunnel release, Lymph Node Biopsy
Ingrown Toenail Surgery
Skin & Soft Tissue Surgery: Skin cancer removal, lipoma and
sebaceous cyst excision
Emergency Surgery: Laparotomy, Appendicectomy, bowel resection
Endoscopy: Diagnostic and therapeutic procedures

```html
<!DOCTYPE html>
<html lang="en">
<head>
<meta charset="utf-8">
<title>Dr Tobias Vanterpool – General &amp; Upper GI Surgeon</title>
<link href="https://fonts.googleapis.com/css2?family=Bebas+Neue&family=Barlow+Condensed:ital,wght@1,400&family=Poppins:wght@400;500;600;700&display=swap" rel="stylesheet">
<style>
:root{
  --navy:#0d3f78;
  --navy-deep:#0b2f5e;
  --blue:#1c6fb8;
  --cyan:#19a2e3;
  --ink:#1f2d3d;
  --stage:#eceef1;
  --strip:#eef1f5;
  --white:#ffffff;
}
*{margin:0;padding:0;box-sizing:border-box}
html,body{width:1200px;height:648px;overflow:hidden;background:var(--stage)}
body{font-family:'Poppins',sans-serif;color:var(--ink)}
.flyer{position:absolute;left:371px;top:0;width:457px;height:648px;overflow:hidden;
  background:linear-gradient(160deg,#ffffff 0%,#f4f9fe 55%,#e4f1fc 100%)}
.profile-column{position:absolute;left:18px;top:0;width:148px;height:546px;
  background:linear-gradient(180deg,#2f6fb4 0%,#1d63ad 45%,#1a86cf 80%,#22a5e4 100%)}
.portrait{position:absolute;left:0;top:0;width:148px;height:290px;
  background:linear-gradient(180deg,#5d8fc6 0%,#3a74b6 60%,#2767ae 100%)}
.doctor-name{position:absolute;left:6px;top:300px;font-family:'Bebas Neue',sans-serif;
  font-size:35px;line-height:34px;color:var(--white);letter-spacing:.3px;font-weight:400}
.name-rule{position:absolute;left:6px;top:411px;width:97px;height:3px;background:var(--navy)}
.specialty{position:absolute;left:6px;top:419px;font-family:'Barlow Condensed',sans-serif;
  font-style:italic;font-size:19px;line-height:19px;color:var(--white);letter-spacing:.2px}
.contact-panel{position:absolute;left:0;top:546px;width:219px;height:102px;background:var(--navy);
  padding:12px 0 0 17px;color:var(--white);font-size:7.6px;line-height:12.3px;font-style:normal}
.contact-row{display:flex;align-items:flex-start;gap:5px}
.contact-row svg{width:8px;height:8px;margin-top:2px;flex:none;fill:var(--white)}
.contact-row.indent{padding-left:13px}
.intro{position:absolute;left:188px;top:28px;width:246px}
.section-label{font-size:12.4px;font-weight:700;color:var(--cyan);letter-spacing:.2px;line-height:16px}
.intro p{font-size:7.7px;line-height:10.75px;margin-top:3px;margin-bottom:3px}
.personal-band{position:absolute;left:166px;top:225px;width:266px;height:55px;background:var(--navy);
  padding:5px 0 0 22px;color:var(--white)}
.personal-band .lead{font-size:10.4px;font-weight:600;color:var(--cyan);line-height:11px}
.personal-band p{font-size:9px;line-height:10.6px}
.expertise{position:absolute;left:188px;top:294px;width:260px}
.expertise h2{font-size:15.4px;font-weight:700;color:var(--navy);letter-spacing:.4px;line-height:19px}
.expertise h3{font-size:11px;font-weight:600;color:var(--cyan);line-height:14px;margin-top:3px}
.expertise ul{list-style:none;font-size:7.7px;line-height:10.75px}
.expertise li{position:relative;padding-left:11px}
.expertise li::before{content:"";position:absolute;left:2px;top:3.6px;width:3.4px;height:3.4px;border-radius:50%;background:var(--blue)}
.expertise li.plain::before{display:none}
.expertise .topic{color:var(--cyan);font-weight:600}
.accreditation-strip{position:absolute;left:219px;top:569px;width:238px;height:60px;background:var(--strip);
  display:flex;align-items:center;gap:8px;padding-left:10px}
.badge{width:28px;height:28px;border-radius:50%;background:#3cbfa0;flex:none}
.org-name{font-size:6.4px;line-height:8px;color:var(--navy);font-weight:500}
.org-mark{width:10px;height:12px;background:var(--navy);flex:none}
</style>
</head>
<body>
<main class="flyer">
  <section class="profile-column">
    <div class="portrait" role="img" aria-label="Portrait photograph of Dr Tobias Vanterpool in suit and tie"></div>
    <h1 class="doctor-name">Dr. Tobias<br>Vanterpool<br>MD, FHCS</h1>
    <div class="name-rule"></div>
    <p class="specialty">GENERAL &amp;<br>UPPER GI SURGEON</p>
  </section>

  <section class="intro">
    <h2 class="section-label">INTRODUCING</h2>
    <p>Tobias is a highly trained general surgeon, having completed extensive surgical training at Coralbay health, Fenwick and Thornleigh Health networks. He further specialized by completing a fellowship in Oesophagogastric and Bariatric Surgery at Larkspur Hospital Northgate, one of Northridge’s leading Upper GI surgical centres.</p>
    <p>With expertise in both advanced laparoscopic and open surgical techniques, he performs a wide range of procedures involving the gastrointestinal system, abdominal wall hernias, as well as other major and minor general surgical operations. In addition to holding appointments at Coralbay Health, he also operates at Brindle and Quarrydale Private Hospitals.</p>
    <p>Dr Vanterpool is committed to providing patient-centred care with a focus on surgical precision, safety, and long-term health outcomes.</p>
  </section>

  <section class="personal-band">
    <p class="lead">He is also fluent in Farsi/Pesrian.</p>
    <p>Outside of surgery, Tobias enjoys playings classical piano and spending time with his 6-year-old Bordoodle on long walks.</p>
  </section>

  <section class="expertise">
    <h2>SURGICAL EXPERTISE</h2>
    <h3>Upper GI &amp; Bariatric Surgery</h3>
    <ul>
      <li>Hiatus hernia repair</li>
      <li>Sleeve gastrectomy</li>
      <li>Gastric bypass</li>
    </ul>
    <h3>General Surgery</h3>
    <ul>
      <li><span class="topic">Gallbladder Surgery</span></li>
      <li class="plain">Laparoscopic cholecystectomy</li>
      <li><span class="topic">Hernia Repair</span></li>
      <li class="plain">Laparoscopic &amp; open surgery (inguinal, umbilical, incisional)</li>
      <li><span class="topic">Anorectal Procedures</span></li>
      <li class="plain">Haemorrhoidectomy, haemorrhoid banding</li>
      <li><span class="topic">Hand Surgery</span></li>
      <li class="plain">Carpal tunnel release, lymph node biopsy</li>
      <li class="plain">Ingrown Toenail Surgery</li>
      <li><span class="topic">Skin &amp; Soft Tissue Surgery</span></li>
      <li class="plain">Skin cancer removal, lipoma &amp; sebaceous cyst excision</li>
      <li><span class="topic">Emergency Surgery</span></li>
      <li class="plain">Laparotomy, appendicectomy, bowel resection</li>
      <li class="plain">Endoscopy: Diagnostic &amp; therapeutic procedures</li>
    </ul>
  </section>

  <address class="contact-panel">
    <div class="contact-row"><svg viewBox="0 0 10 10"><path d="M5 0a3.5 3.5 0 0 0-3.5 3.5C1.5 6 5 10 5 10s3.5-4 3.5-6.5A3.5 3.5 0 0 0 5 0zm0 4.8a1.3 1.3 0 1 1 0-2.6 1.3 1.3 0 0 1 0 2.6z"/></svg><span>Suite 4C, Brindle Private Hospital</span></div>
    <div class="contact-row indent"><span>518 Cobbler Parade, Ashcombe, NRD, 4870</span></div>
    <div class="contact-row"><svg viewBox="0 0 10 10"><path d="M2 0.5l2 2-1 1.3a6 6 0 0 0 3.2 3.2L7.5 6l2 2-1.3 1.5C4.5 9.5.5 5.5.5 1.8z"/></svg><span>(03) 9587 1062</span></div>
    <div class="contact-row"><svg viewBox="0 0 10 10"><path d="M2.5 0h4l1 1v2h1a1 1 0 0 1 1 1v5H.5V4a1 1 0 0 1 1-1h1zm1 1v2h3V1zm0 4v1h3V5z"/></svg><span>(03) 9316 4471</span></div>
    <div class="contact-row"><svg viewBox="0 0 10 10"><path d="M0 1.5h10v7H0zm1 1l4 3 4-3v-.1H1z"/></svg><span>referrals@lanternoperativeclinic.com.au</span></div>
    <div class="contact-row"><svg viewBox="0 0 10 10"><path d="M5 0a5 5 0 1 0 0 10A5 5 0 0 0 5 0zm3.9 4.5H7.1a7 7 0 0 0-.8-3.3 4 4 0 0 1 2.6 3.3zM5 1c.6.7 1 2 1.1 3.5H3.9C4 3 4.4 1.7 5 1zM3.7 1.2a7 7 0 0 0-.8 3.3H1.1a4 4 0 0 1 2.6-3.3zM1.1 5.5h1.8a7 7 0 0 0 .8 3.3 4 4 0 0 1-2.6-3.3zM5 9c-.6-.7-1-2-1.1-3.5h2.2C6 7 5.6 8.3 5 9zm1.3-.2a7 7 0 0 0 .8-3.3h1.8a4 4 0 0 1-2.6 3.3z"/></svg><span>www.lanternoperativeclinic.com.au</span></div>
  </address>

  <section class="accreditation-strip">
    <div class="badge" aria-hidden="true"></div>
    <span class="org-name">Surgeons<br>Guild</span>
    <div class="org-mark" aria-hidden="true"></div>
    <span class="org-name">Fellow of the Harbourline<br>College of Surgeons</span>
  </section>
</main>
</body>
</html>
```